Medical Laboratory Banner design needed

I need a marketing design for a retractable banner that measures 33" wide by 81" high. We are a medical laboratory that provides diagnostic testing to thousands of health care professionals and their patients. Currently we are providing Covid-19 testing as well and are operating mobile collection sites across the country. I would like to have these banners at those sites. The banner should give an onlooker a good understanding of who Harbor Crest Laboratories is and what we offer. The banners should use the color scheme from our logo. I have attached some initial concepts and thoughts. Our website - www.harborcrestlabs.example can be used for information as well.

```html
<!DOCTYPE html>
<html lang="en">
<head>
<meta charset="UTF-8">
<title>Harbor Crest Laboratories – Retractable Banner</title>
<link rel="stylesheet" href="https://fonts.googleapis.com/css2?family=Montserrat:wght@400;500;600;700;900&display=swap">
<style>
  :root {
    --page-bg: #eef0f1;
    --white: #ffffff;
    --brand-green: #3b8b79;
    --brand-navy: #1f2466;
    --teal-light: #21cdd0;
    --teal-mid: #1bb2b4;
    --teal-deep: #16898c;
    --icon-line: #e8fbfb;
  }
  * { box-sizing: border-box; margin: 0; padding: 0; }
  html, body {
    width: 800px; height: 1200px; overflow: hidden;
    background: var(--page-bg);
    font-family: "Montserrat", Arial, sans-serif;
  }
  .banner {
    position: absolute; left: 164px; top: 20px;
    width: 472px; height: 1160px;
    background: var(--white);
    box-shadow: 0 6px 24px rgba(0,0,0,0.12);
    overflow: hidden;
  }
  .brand { position: absolute; top: 30px; left: 0; right: 0; text-align: center; }
  .brand-dot {
    width: 30px; height: 30px; border-radius: 50%;
    background: var(--brand-navy); margin: 0 auto 12px;
  }
  .brand-name {
    font-weight: 700; font-size: 17px; color: var(--brand-navy);
    letter-spacing: 0.2px;
  }
  .brand-url {
    margin-top: 8px; font-size: 13px; font-weight: 500; color: var(--brand-green);
  }
  .headline {
    position: absolute; top: 172px; left: 0; right: 0; text-align: center;
    font-weight: 900; font-size: 46px; line-height: 1; letter-spacing: -0.5px;
    color: var(--brand-green);
  }
  .mission {
    position: absolute; top: 241px; left: 0; right: 0; text-align: center;
    font-weight: 500; font-size: 22px; line-height: 30px; letter-spacing: 1px;
    color: var(--brand-green);
  }
  .mission-focus {
    position: absolute; top: 316px; left: 0; right: 0; text-align: center;
    font-weight: 700; font-size: 24px; letter-spacing: 0.8px;
    color: var(--brand-navy);
  }
  .offer-panel {
    position: absolute; top: 370px; left: 0; width: 100%; height: 723px;
    background: linear-gradient(180deg, var(--teal-light) 0%, var(--teal-mid) 45%, var(--teal-deep) 100%);
  }
  .offer-title {
    position: absolute; top: 20px; left: 0; right: 0; text-align: center;
    font-weight: 700; font-size: 28px; letter-spacing: 1.5px; color: var(--white);
  }
  .service {
    position: absolute; top: 89px; width: 150px; text-align: center;
  }
  .service--pcr { left: 55px; }
  .service--antibody { left: 267px; }
  .service-icon {
    width: 90px; height: 74px; margin: 0 auto;
    border: 1.5px dashed rgba(255,255,255,0.75); border-radius: 4px;
    display: flex; align-items: center; justify-content: center;
  }
  .service-label {
    margin-top: 14px; font-weight: 500; font-size: 18px; line-height: 22px;
    letter-spacing: 0.6px; color: var(--white);
  }
  .virus-visual {
    position: absolute; top: 255px; left: 36px; width: 400px; height: 430px;
    border-radius: 50%;
    background: radial-gradient(circle at 50% 48%, #0f5e5a 0%, #1a7e78 38%, #2aa8a5 62%, rgba(33,180,182,0) 74%);
  }
  .contact-bar {
    position: absolute; bottom: 0; left: 0; width: 100%; height: 67px;
    background: var(--brand-navy);
    display: flex; align-items: center; justify-content: center; gap: 12px;
    color: var(--white); font-weight: 500; font-size: 20px; letter-spacing: 0.6px;
  }
</style>
</head>
<body>
  <main class="banner">
    <header class="brand">
      <div class="brand-dot"></div>
      <div class="brand-name">HARBOR CREST LABORATORIES</div>
      <div class="brand-url">www.harborcrestlabs.example</div>
    </header>

    <h1 class="headline">HARBOR CREST</h1>
    <p class="mission">LABORATORIES IS DEDICATED<br>TO HELP COMBAT</p>
    <p class="mission-focus">THE NOVEL COVID-19 VIRUS</p>

    <section class="offer-panel">
      <h2 class="offer-title">WE OFFER</h2>

      <div class="service service--pcr">
        <div class="service-icon">
          <svg width="48" height="50" viewBox="0 0 48 50" fill="none" stroke="var(--icon-line)" stroke-width="2" stroke-linecap="round" stroke-linejoin="round">
            <rect x="20" y="4" width="8" height="18" rx="2"/>
            <path d="M24 22v6"/>
            <path d="M30 12c8 2 10 12 6 20"/>
            <circle cx="13" cy="24" r="5"/>
            <path d="M18 34h18"/>
            <rect x="10" y="40" width="28" height="5" rx="1"/>
            <path d="M32 32v8"/>
          </svg>
        </div>
        <p class="service-label">BOTH PCR<br>TESTING</p>
      </div>

      <div class="service service--antibody">
        <div class="service-icon">
          <svg width="48" height="52" viewBox="0 0 48 52" fill="none" stroke="var(--icon-line)" stroke-width="2" stroke-linecap="round" stroke-linejoin="round">
            <path d="M21 48V28L8 12"/>
            <path d="M27 48V28L40 12"/>
            <path d="M15 32L4 18"/>
            <path d="M33 32L44 18"/>
            <path d="M21 48h6"/>
          </svg>
        </div>
        <p class="service-label">ANTIBODY<br>TESTING</p>
      </div>

      <div class="virus-visual" role="img" aria-label="Close-up illustration of a coronavirus particle with spike proteins on a teal background"></div>
    </section>

    <footer class="contact-bar">
      <svg width="20" height="20" viewBox="0 0 24 24" fill="var(--white)" aria-hidden="true">
        <path d="M6.6 10.8a15.1 15.1 0 0 0 6.6 6.6l2.2-2.2c.3-.3.7-.4 1-.2 1.1.4 2.3.6 3.6.6.6 0 1 .4 1 1V20c0 .6-.4 1-1 1A17 17 0 0 1 3 4c0-.6.4-1 1-1h3.5c.6 0 1 .4 1 1 0 1.3.2 2.5.6 3.6.1.3 0 .7-.2 1l-2.3 2.2z"/>
      </svg>
      <span>555-LAB-0142 (555-522-0142)</span>
    </footer>
  </main>
</body>
</html>
```